Flyer-Design für Hundephysiopraxis
Zielgruppe
Ich bin selbstständige Hundephysiotherapeutin / Hundeosteopathin /Hundefitnesstrainerin. Meine Zielgruppe sind Hundehalter bzw. allgemein Tierhalter (biete noch weitere Dinge für Hunde/Tiere an) aber auch Tierärzte.
Aufgabenstellung
Es wäre schön, wenn Sie die Texte ähnlich wie auf meiner Homepage gestalten (z.B. Infos aus der Startseite oder Therapieformen).
Prinzipiell sollte es eher natürlich, freundlich und nett gestaltet sein. Schlichtere Farben passend zum Logo.
Homepage: www.pfotenwohlsein-muster.de
Bei den Maßen bin ich offen, hatte aber eher an diesen 'typischen Flyer' gedacht (3 seitiger Flyer mit Vorder und Rückseite) bin aber prinzipiell offen :)
Einen Beispiel Flyer habe ich drangehängt sowie z.B. schon ein paar Fotos die man ggf nutzen kann. Weitere Behandlunsfotos kann ich gerne nachreichen.
Die Flyer sollen hauptsächlich bei z.B. Tierärzten / Tierklinik / Tiernahrungsmärkte wie Napfkorb ausgelegt werden damit Menschen die mich noch nicht kennen auf meine Arbeit aufmerksam werden.

```html
<!DOCTYPE html>
<html lang="de">
<head>
<meta charset="utf-8">
<title>Pfotenwohlsein – Flyer</title>
<link rel="stylesheet" href="https://fonts.googleapis.com/css2?family=Cormorant+Garamond:wght@400;600;700&family=Dancing+Script:wght@400&display=swap">
<style>
  :root{
    --page:#f2f2f0;
    --sand:#d9ccb6;
    --sand-dark:#cdbd9f;
    --cream:#efe5d3;
    --light:#f7f1e6;
    --white:#ffffff;
    --orange:#d0742c;
    --photo-green:#8d9a6a;
    --photo-warm:#b8a58a;
    --serif:"Cormorant Garamond", Georgia, serif;
    --script:"Dancing Script", cursive;
  }
  *{box-sizing:border-box;margin:0;padding:0}
  html,body{width:1200px;height:848px;overflow:hidden}
  body{background:var(--page);position:relative;font-family:var(--serif);color:var(--orange)}
  .spread{position:absolute;top:216px;width:588px;height:416px;background:var(--sand);overflow:hidden;box-shadow:0 3px 10px rgba(0,0,0,.18)}
  .spread--outside{left:6px}
  .spread--inside{left:606px}
  .panel{position:absolute;top:0;height:416px;width:196px}
  .panel--1{left:0}.panel--2{left:196px}.panel--3{left:392px}
  .wave{position:absolute;inset:0;width:588px;height:416px}
  .photo{position:absolute;overflow:hidden}
  .copy{position:absolute;font-size:5.3px;line-height:1.4;color:var(--orange)}
  .copy p{margin-bottom:3px}
  .heading{font-weight:700;font-size:8px;line-height:1.2;color:var(--orange)}
  .list{list-style:none;font-size:5.8px;line-height:1.55}
  .list li::before{content:"- "}
  .script{font-family:var(--script);color:var(--orange)}
  .center{text-align:center}

  /* outside */
  .intro{left:96px;top:10px;width:92px}
  .uses{left:10px;top:118px;width:180px}
  .uses .heading{margin-bottom:6px}
  .offer-script{position:absolute;left:10px;top:322px;font-size:10px;line-height:1.35;transform:rotate(-4deg)}
  .qualifications{left:206px;top:14px;width:176px;font-size:4.6px}
  .qualifications h3{font-size:5.6px;font-weight:700;margin-bottom:2px}
  .qualifications .block{margin-bottom:6px}
  .contact{left:206px;top:212px;width:90px;font-size:4.6px}
  .brand{position:absolute;left:392px;top:18px;width:196px;text-align:center}
  .brand-mark{display:inline-block;width:18px;height:18px;border-radius:50%;background:var(--orange);margin-bottom:3px}
  .brand-name{font-size:15px;font-weight:600;line-height:1}
  .brand-sub{font-size:4.8px;margin-top:2px}
  .services{position:absolute;left:396px;top:322px;width:188px;font-size:8.4px;line-height:1.55;text-align:center}
  .web{position:absolute;left:392px;top:388px;width:196px;font-size:8px;text-align:center}

  /* inside */
  .claim{position:absolute;left:18px;top:10px;font-size:11px;line-height:1.3;transform:rotate(-6deg)}
  .story{left:10px;top:92px;width:178px}
  .vital{left:204px;top:190px;width:180px}
  .vital .heading{margin-bottom:6px}
  .quote{position:absolute;left:222px;top:362px;width:150px;font-size:8px;line-height:1.25;text-align:center;transform:rotate(-3deg)}
  .method{left:400px;top:12px;width:180px}
  .method .heading{margin-bottom:5px}
</style>
</head>
<body>

<!-- Außenseite -->
<section class="spread spread--outside">
  <svg class="wave" viewBox="0 0 588 416" aria-hidden="true">
    <path d="M196 0 H392 V416 H196 Z" fill="#e3d7c2"/>
    <path d="M392 0 H588 V70 C550 95 500 60 460 85 C430 100 405 80 392 90 Z" fill="#f7f1e6"/>
    <path d="M392 300 C430 280 470 310 520 295 C550 286 570 300 588 292 V416 H392 Z" fill="#efe5d3"/>
    <path d="M0 300 C40 290 80 320 130 300 C160 290 185 300 196 292 V416 H0 Z" fill="#ffffff"/>
  </svg>

  <div class="photo" role="img" aria-label="Foto: Therapeutin behandelt einen Hund auf einer Decke" style="left:8px;top:6px;width:82px;height:104px;border-radius:50%;background:linear-gradient(160deg,#c9bba4,#7c6f62)"></div>
  <div class="copy intro">
    <p>Für mich steht Dein Hund an erster Stelle! Ich habe selbst Erfahrungen mit Hundeschmerzen, sowie Hunden aus deutscher Zucht und weiß, dass manche Hunde „ihr Päckchen“ zu tragen haben. Dabei steht im Fokus, dass sich Dein Vierbeiner bei mir wohlfühlt, er mir Vertrauen schenkt und gerne zur Physiotherapie geht.</p>
  </div>
  <div class="copy uses">
    <h2 class="heading">Einsatzmöglichkeiten der Physiotherapie:</h2>
    <ul class="list">
      <li>Schmerzlinderung</li>
      <li>Muskelaufbau</li>
      <li>Konditionssteigerung</li>
      <li>Konditionserhalt</li>
      <li>Verbesserung der Beweglichkeit (Sehnen, Bänder und Gelenke)</li>
      <li>Lösen von Blockaden</li>
      <li>Prävention</li>
      <li>Gangschulung</li>
      <li>Nachsorge nach Operationen</li>
      <li>Wundheilungsstörungen</li>
      <li>Muskelverspannungen</li>
      <li>neurologische Erkrankungen</li>
      <li>degenerative Erkrankungen</li>
    </ul>
  </div>
  <p class="offer-script script">Hundephysiotherapie<br>Hundeosteopathie<br>Dorn-Therapie und Breuss Massage<br>Hundefitnesstrainer</p>

  <div class="copy qualifications center">
    <h3>Meine Qualifikationen</h3>
    <div class="block">Ausbildungen:<br>Frühjahr 2022 erfolgreich abgeschlossene Ausbildung zur Hundephysiotherapeutin an einer Fachschule<br>Frühjahr 2022 erfolgreich abgeschlossene Ausbildung zur Hundeosteopathin an einer Akademie</div>
    <div class="block">Veterinärmedizinische Grundlagen:<br>Sommer 2021 Grundlagenkurs in Anatomie und Bewegungslehre<br>Herbst 2021 Landesprüfung beim Veterinäramt bestanden</div>
    <div class="block">Weiterbildungen und Fortbildungen:<br>Frühjahr 2022 Kurs Dorn-Therapie<br>Sommer 2022 Kurs Breuss Massage und sanfte Wirbelsäulenarbeit<br>Sommer 2022 Seminar Tierkommunikation mit praktischem Teil<br>Herbst 2022 Kurs Blutegeltherapie und Mykotherapie<br>Herbst 2022 Fortbildung Bachblüten und Edelsteintherapie</div>
    <div class="block">Weitere Ausbildungen und Kurse sind in Planung, damit ich Deinem Hund stets die bestmögliche Therapie bieten kann.</div>
  </div>
  <div class="copy contact">
    Kontakt:<br>
    www.pfotenwohlsein-muster.de<br>
    kontakt@pfotenwohlsein-muster.de<br>
    Praxis Pfotenwohlsein<br>
    Wiesenweg 12<br>
    12345 Musterstadt<br>
    0123 456789
  </div>
  <div class="photo" role="img" aria-label="Foto: Therapeutin kniet im Gras und behandelt einen liegenden Spaniel" style="left:200px;top:266px;width:180px;height:136px;border-radius:46% 40% 8px 8px / 40% 34% 8px 8px;background:linear-gradient(170deg,#a9b07d,#6f7650 60%,#4c4a45)"></div>

  <div class="brand">
    <span class="brand-mark"></span>
    <div class="brand-name">Pfotenwohlsein</div>
    <div class="brand-sub">Hundephysiotherapie Lena Muster</div>
  </div>
  <div class="photo" role="img" aria-label="Foto: schwarz-weißer Spaniel sitzt im Gras" style="left:388px;top:92px;width:180px;height:212px;border-radius:40% 30% 34% 26% / 20% 22% 26% 24%;background:linear-gradient(170deg,#6e7a55,#303030 50%,#8d9a6a)"></div>
  <p class="services">Hundephysiotherapie • Hundeosteopathie<br>Hundefitnesstrainerin • Bachblütenberaterin<br>Tierkommunikation • Mykotherapie<br>Edelsteintherapie</p>
  <p class="web">www.pfotenwohlsein-muster.de</p>
</section>

<!-- Innenseite -->
<section class="spread spread--inside">
  <svg class="wave" viewBox="0 0 588 416" aria-hidden="true">
    <path d="M0 0 H196 V60 C170 80 120 70 80 90 C50 104 20 90 0 100 Z" fill="#ffffff"/>
    <path d="M196 0 H392 V416 H196 Z" fill="#efe5d3"/>
    <path d="M392 0 H588 V416 H392 Z" fill="#d9ccb6"/>
    <path d="M196 340 C240 330 300 360 392 340 V416 H196 Z" fill="#ffffff"/>
  </svg>

  <p class="claim script">Leben ist Bewegung und<br>Bewegung ist Lebensqualität!</p>
  <div class="copy story">
    <p>Rennen, hüpfen, springen, toben und spielen zeigt die Lebensfreude unserer Hunde!<br>Wer keine Schmerzen hat, kann sich frei bewegen und hat Spaß dabei.<br>Wenn unsere Hunde jedoch erkranken oder alt werden, dann benötigen sie unsere Unterstützung.</p>
    <p>Nach einem Unfall, bei Schmerzen oder Beschwerden im Rücken und in den Gelenken, nach Operationen oder bei Lebensalter können Physiotherapie sowie Osteopathie helfen. Es lindert die Schmerzen, lockert verspannte Muskulatur, verbessert die Beweglichkeit oder stellt diese wieder her. Weiterhin baut Physiotherapie Muskulatur auf, fördert die Genesung und hilft im Alter fit zu bleiben.</p>
    <p>Ich helfe Deinem Hund gerne dabei, die Gesundheit und damit die Lebensqualität und Lebensfreude zu erhalten.</p>
  </div>
  <div class="photo" role="img" aria-label="Foto: Spaniel läuft mit fliegenden Ohren auf die Kamera zu" style="left:10px;top:250px;width:178px;height:160px;border-radius:50% 50% 10px 10px / 40% 40% 10px 10px;background:linear-gradient(180deg,#dfe1da,#b7b8ad 55%,#8d9a6a)"></div>

  <div class="photo" role="img" aria-label="Foto: Spaniel mit braunen Ohren auf einem Tisch" style="left:202px;top:4px;width:184px;height:162px;border-radius:50% 46% 48% 44% / 52% 50% 46% 48%;background:linear-gradient(160deg,#c8c2b4,#6b4a3a 55%,#e8e2d8)"></div>
  <div class="copy vital">
    <h2 class="heading">Doch nicht nur die Hundephysiotherapie verhilft Deinem Hund zu mehr Vitalität ...</h2>
    <p>Ist Dein Hund angeschlagen? Bist gibt es noch gar oder Du weißt um verschiedenes Verhaltensweisen nicht weiter?</p>
    <p>Hier greife zum Beispiel die Tierkommunikation oder Bachblüten. Auch die Vitalpilz-Therapie wird in dem Veterinärbereich immer wichtiger, da hier gute Erfolge erzielt werden, z.B. bei Verdauungsproblemen, Immunstörungen, Allergien, Arthrose, Durchblutungsstörungen oder auch Krebs und Nierenerkrankungen.</p>
    <p>Ist Dein Hund gesund, Du möchtest aber seine Fitness verbessern oder ein paar Kilos sollen schwinden?</p>
    <p>Hier unterstütze ich mich gerne als Hundefitnesstrainer. Wir arbeiten gemeinsam einen Trainingsplan für Deinen Hund heraus. Sei es für den Sportlauf in Agility oder für die Couchpotato.</p>
  </div>
  <p class="quote script">„Lebensfreude lässt sich an besten von Hunden lernen.“</p>

  <div class="copy method">
    <h2 class="heading">Hundephysiotherapie &amp; Hundeosteopathie</h2>
    <p>In der Humanmedizin sind die Physiotherapie bei der Genesung der Patienten schon selbstverständlich und unterstützend eingesetzt. Dies können ein ähnlichen Problemen leiden wie wir Menschen. Sie haben genau so Schmerzen und dies schränkt ihr Leben ebenso ein. Wir können unsere Schmerzen äußern. Viele Hunde jedoch leben mit diesen Schmerzen viele Wochen, die sie immer mehr verstecken und lernen oder andere Dinge anzeigen. Gerade deshalb ist die Physiotherapie so wertvoll, damit unsere Hunde unbeschwert und ohne Schmerzen lange an unserer Seite bleiben.</p>
    <p>Jeder Körper ist ein individuelles und komplexes System mit eigenen Anforderungen an Bewegungsabläufe, Belastungen und Erholungsphasen. Entsprechend umfangreich aufgestellt ist das Therapiespektrum meiner Arbeit. Dabei stehen im Fokus die sanften und individuellen Therapieprogramme in enger Zusammenarbeit mit dem Tierarzt. Sowohl abgestimmt auf die speziellen Anforderungen der einzelnen Krankheitsbilder. Jeder Hund hat eine andere Hintergrundgeschichte und auch dies berücksichtige ich bei meinen Therapien.<br>Mein Ziel ist es, die Lebensfreude und Lebensqualität unserer Vierbeiner zu erhalten oder sie zu verbessern.</p>
  </div>
  <div class="photo" role="img" aria-label="Foto: Therapeutin massiert einen liegenden Spaniel im Garten" style="left:396px;top:252px;width:186px;height:156px;border-radius:48% 44% 10px 10px / 38% 36% 10px 10px;background:linear-gradient(170deg,#9aa572,#5f6448 55%,#5a4a42)"></div>
</section>

</body>
</html>
```